Pet store web design

I would like to redesign my current online store (http://brindlecove.example)
I'm looking for a clean, modern design. Any ideas are welcome..

Industry/Entity Type

Pet

Number of Pages Required

3 page

```html
<!DOCTYPE html>
<html lang="en">
<head>
<meta charset="utf-8">
<title>Brindle Cove – Swashbuckler Pirate Girl Dog Costume</title>
<link href="https://fonts.googleapis.com/css2?family=Open+Sans:wght@400;600;700&family=Raleway:wght@400;600;700&display=swap" rel="stylesheet">
<style>
:root{
  --yellow:#fcd33a;
  --yellow-soft:#fde27a;
  --orange:#f39a1d;
  --bg:#f0f0ee;
  --panel:#ffffff;
  --ink:#3c3c3c;
  --muted:#8a8a8a;
  --line:#dcdcdc;
  --pink:#f6d6dc;
  --blue:#d6e6ee;
  --green:#dfe7cf;
  --mauve:#ecd6dc;
}
*{box-sizing:border-box;margin:0;padding:0}
html,body{width:791px;height:1200px;overflow:hidden}
body{background:var(--bg);font-family:"Open Sans",sans-serif;color:var(--ink);position:relative;font-size:10px}
.abs{position:absolute}
.site-header{left:0;top:0;width:791px;height:76px;background:var(--yellow)}
.brand{left:74px;top:18px;display:flex;align-items:center;gap:8px;font-family:"Raleway",sans-serif;font-weight:700;font-size:22px;color:#fff}
.brand i{width:26px;height:26px;border-radius:50%;background:#fff;display:block}
.main-nav{left:352px;top:44px;display:flex;gap:22px;font-size:9px;font-weight:600;color:#5a4a10;text-transform:uppercase}
.search{left:550px;top:12px;width:70px;height:18px;border-radius:9px;background:#fff;font-size:8px;color:var(--muted);padding:3px 9px}
.social{left:650px;top:12px;display:flex;gap:10px}
.social span{width:16px;height:16px;border-radius:50%;background:#fff}
.product-panel{left:74px;top:104px;width:643px;height:278px;background:var(--panel)}
.back-link{left:16px;top:14px;font-size:8px;color:var(--muted)}
.product-photo{left:14px;top:30px;width:210px;height:230px;background:radial-gradient(circle at 50% 45%,#e8c9b0,#c22a2a 45%,#f4f0ec 75%)}
.product-title{left:242px;top:14px;width:250px;font-family:"Raleway",sans-serif;font-weight:700;font-size:15px;line-height:19px}
.stock{left:560px;top:16px;font-size:13px;color:var(--orange);font-weight:600}
.price{left:242px;top:60px;font-size:17px;color:var(--orange);font-weight:600}
.qty{left:500px;top:62px;font-size:13px;font-weight:600;display:flex;align-items:center;gap:10px}
.qty b{width:38px;height:18px;border:1px solid var(--line);border-radius:9px;font-size:9px;font-weight:400;padding:2px 8px}
.tabs{left:242px;top:92px;width:380px;border-bottom:1px solid var(--line);display:flex;gap:18px;font-size:9px;color:var(--muted);text-transform:uppercase;padding-bottom:4px}
.tabs .on{color:var(--ink);font-weight:600}
.desc{left:242px;top:116px;width:380px;font-size:8.5px;line-height:13px;color:var(--muted)}
.sizes{left:242px;top:180px;display:flex;align-items:center;gap:22px;font-size:8px;color:var(--muted)}
.sizes strong{font-size:13px;color:var(--ink)}
.sizes span::before{content:"";display:inline-block;width:8px;height:8px;border-radius:50%;border:1px solid #aaa;margin-right:4px;vertical-align:-1px}
.btn{display:inline-block;border-radius:12px;font-size:8.5px;text-align:center;line-height:22px;height:24px}
.btn-outline-o{border:1px solid var(--orange);color:var(--orange)}
.btn-outline{border:1px solid #999;color:var(--ink)}
.actions{left:242px;top:208px;display:flex;gap:16px}
.actions .btn{width:82px}
.band{left:74px;width:643px;height:32px;background:var(--yellow-soft);font-family:"Raleway",sans-serif;font-weight:600;font-size:14px;text-align:center;line-height:32px;letter-spacing:1px;color:#4a4a4a}
.carousel{left:74px;top:432px;width:643px;height:214px}
.arrow{top:82px;width:12px;height:20px}
.cards{left:20px;top:0;display:flex;gap:12px}
.card{width:139px;height:214px;background:var(--panel);position:relative;text-align:center}
.card .pic{height:110px;margin:8px}
.card h4{font-size:8px;font-weight:600;margin-top:6px}
.card p{font-size:8px;color:var(--muted);margin-top:3px}
.card .foot{position:absolute;left:0;bottom:0;width:100%;height:52px;padding-top:14px}
.card .btn{width:70px;height:20px;line-height:18px;border:1px solid #888;background:#fff}
.review{left:74px;top:716px;width:643px;height:240px}
.review .lead{font-size:9px;color:var(--ink)}
.review .ask{top:30px;font-size:8.5px;font-weight:600}
.rating{left:0;top:60px;border-collapse:collapse;font-size:8.5px}
.rating td{width:28px;height:32px;text-align:center}
.rating td:first-child{width:60px;text-align:left;font-weight:600}
.dot{display:inline-block;width:12px;height:12px;border-radius:50%;border:1px solid #bbb;background:#fff}
.dot.on{background:#ccc}
.field{left:330px;width:300px;height:24px;background:#fff;border:1px solid var(--line);border-radius:12px;font-size:8.5px;color:var(--muted);padding:5px 12px}
.field.area{height:80px;border-radius:12px}
.submit{left:335px;top:208px;width:118px;background:var(--yellow);font-weight:700;color:#5a4a10}
.newsletter{left:74px;top:966px;width:643px;height:34px;border-bottom:1px solid var(--line);font-size:8.5px;font-weight:600;line-height:26px}
.newsletter em{font-style:normal;color:var(--orange);margin-left:6px}
.newsletter .field{left:510px;top:2px;width:133px;height:22px;padding:4px 10px;font-weight:400}
.site-footer{left:0;top:1010px;width:791px;height:170px;background:#fff}
.col{top:22px;font-size:8px;line-height:15px;color:var(--muted)}
.col h5{font-size:8.5px;color:var(--ink);font-weight:700;margin-bottom:6px;text-transform:uppercase}
.col li{list-style:none}
.col li::before{content:"›";color:var(--orange);margin-right:5px}
.about p{width:150px;line-height:12px}
.pay{display:flex;gap:8px;margin-top:6px}
.pay span{width:34px;height:22px;border-radius:3px;background:#e4e4e4}
.copyright{left:0;top:1180px;width:791px;height:20px;background:var(--yellow);font-size:8px;text-align:center;line-height:20px;color:#5a4a10}
</style>
</head>
<body>
<header class="abs site-header">
  <div class="abs brand"><i></i>Brindle Cove</div>
  <div class="abs search">Search</div>
  <div class="abs social"><span></span><span></span><span></span></div>
  <nav class="abs main-nav"><span>My Account</span><span>My Cart</span><span>Checkout</span><span>My Wishlist</span><span>Log In/Register</span></nav>
</header>

<section class="abs product-panel">
  <div class="abs back-link">‹ Back to products</div>
  <div class="abs product-photo" role="img" aria-label="Photo of a small dog wearing a red and black pirate girl costume"></div>
  <h1 class="abs product-title">SWASHBUCKLER PIRATE GIRL DOG COSTUME</h1>
  <div class="abs stock">In Stock</div>
  <div class="abs price">$49.47</div>
  <div class="abs qty">QUANTITY <b>1 ▾</b></div>
  <div class="abs tabs"><span class="on">Description</span><span>Ratings</span><span>Reviews</span></div>
  <p class="abs desc">Set sail in style with this charming costume, trimmed with soft satin, a ruffled skirt and a matching hat. Lightweight fabric keeps your pup comfortable while adding a bold look for parties, parades and playful photos.</p>
  <div class="abs sizes"><strong>SIZE</strong><span>Extra Small</span><span>Small</span><span>Medium</span><span>Large</span></div>
  <div class="abs actions"><span class="btn btn-outline-o">Add to Cart</span><span class="btn btn-outline">Add to Wishlist</span></div>
</section>

<h2 class="abs band" style="top:380px">FEATURED PRODUCTS</h2>

<section class="abs carousel">
  <svg class="abs arrow" style="left:0" viewBox="0 0 12 20"><path d="M9 2 2 10l7 8" fill="none" stroke="#777" stroke-width="2"/></svg>
  <svg class="abs arrow" style="right:0" viewBox="0 0 12 20"><path d="M3 2l7 8-7 8" fill="none" stroke="#777" stroke-width="2"/></svg>
  <div class="abs cards">
    <div class="card"><div class="pic" role="img" aria-label="Dog in a pink tutu costume" style="background:linear-gradient(#f3c9d2,#e8e8e8)"></div><h4>Cutie Bunny Dog Costume</h4><p>$29.47</p><div class="foot" style="background:var(--pink)"><span class="btn">Add to Cart</span></div></div>
    <div class="card"><div class="pic" role="img" aria-label="Dog in a pirate captain costume" style="background:linear-gradient(#c45a4a,#e8e8e8)"></div><h4>Pirate Captain Dog Costume</h4><p>$29.47</p><div class="foot" style="background:var(--blue)"><span class="btn">Add to Cart</span></div></div>
    <div class="card"><div class="pic" role="img" aria-label="Dog in a yellow and black bee costume" style="background:linear-gradient(#d9b233,#3a3a3a)"></div><h4>Honey Bee Dog Costume</h4><p>$29.47</p><div class="foot" style="background:var(--green)"><span class="btn">Add to Cart</span></div></div>
    <div class="card"><div class="pic" role="img" aria-label="Dog in a dark cape costume" style="background:linear-gradient(#5a3a3a,#e8e8e8)"></div><h4>Vampire Dog Costume</h4><p>$29.47</p><div class="foot" style="background:var(--mauve)"><span class="btn">Add to Cart</span></div></div>
  </div>
</section>

<h2 class="abs band" style="top:672px">WRITE YOUR OWN REVIEW</h2>

<section class="abs review">
  <p class="abs lead">You're reviewing: <b>Swashbuckler Pirate Girl Dog Costume</b></p>
  <p class="abs ask">HOW DO YOU RATE THIS PRODUCT?</p>
  <table class="abs rating">
    <tr><td></td><td>1</td><td>2</td><td>3</td><td>4</td><td>5</td></tr>
    <tr><td>VALUE</td><td><i class="dot"></i></td><td><i class="dot"></i></td><td><i class="dot on"></i></td><td><i class="dot"></i></td><td><i class="dot"></i></td></tr>
    <tr><td>QUALITY</td><td><i class="dot"></i></td><td><i class="dot"></i></td><td><i class="dot"></i></td><td><i class="dot on"></i></td><td><i class="dot"></i></td></tr>
    <tr><td>PRICE</td><td><i class="dot"></i></td><td><i class="dot"></i></td><td><i class="dot"></i></td><td><i class="dot on"></i></td><td><i class="dot"></i></td></tr>
  </table>
  <div class="abs field" style="top:22px">Nickname</div>
  <div class="abs field" style="top:56px">Summary of Your Review</div>
  <div class="abs field area" style="top:90px">Review</div>
  <span class="abs btn submit">SUBMIT REVIEW</span>
</section>

<div class="abs newsletter">SIGN UP TO GET ON THE LATEST FROM BRINDLECOVE<em>SIGN UP NOW</em><div class="abs field">Enter email address</div></div>

<footer class="abs site-footer">
  <div class="abs col" style="left:74px"><h5>Services</h5><ul><li>Pet Grooming</li><li>Pet Adoption</li><li>Pet Dog Walker</li><li>Pet Hotels</li><li>Doggy School</li></ul></div>
  <div class="abs col" style="left:240px"><h5>Shopping Online</h5><ul><li>Delivery Information</li><li>Privacy Policy</li><li>Returns Policy</li><li>Terms and Conditions</li><li>FAQs</li></ul></div>
  <div class="abs col" style="left:404px"><h5>&nbsp;</h5><ul><li>About Us</li><li>Careers</li><li>Pet Blog</li><li>Contact Us</li></ul></div>
  <div class="abs col about" style="left:565px"><h5>Brindle Cove</h5><p>Every order is packed with care and shipped fast, so your pets get what they love. Join our club for tips and special offers.</p><h5 style="margin-top:10px">We Accept</h5><div class="pay"><span></span><span></span><span></span></div></div>
</footer>
<div class="abs copyright">© 2015 Brindle Cove. All rights reserved.</div>
</body>
</html>
```